Social Media Monitoring Web Site Design

We need a responsive web design for a new company based in Ireland. We offer a social media monitoring service that works in a call centre environment. Our service name is 'TROVA'. We have a logo that is attached.

Sites we like (in no particular order):

1. http://www.lumengrove.com/
2. https://quillnest.io/
3. https://www.markoriel.com/

We want the web site to have the following sections:

HOME
TROVA PLATFORM
TROVA SERVICE
CASE STUDIES
ABOUT US
CONTACT US

We also need a customer Login link. The site must be a responsive design.

Target Market(s)

Corporate Customers

Industry/Entity Type

It Company

Coding

Coded - Design and coding required

Number of Pages Required

2 page

Requirements
Must have
• Responsive Design
• Bootstrap
Nice to have
• Animations

```html
<!DOCTYPE html>
<html lang="en">
<head>
<meta charset="utf-8">
<title>TROVA – Social Media Monitoring</title>
<link href="https://fonts.googleapis.com/css2?family=Source+Sans+3:wght@400;600;700&family=Arimo:wght@400;700&display=swap" rel="stylesheet">
<style>
:root{
  --black:#0b0b0b;
  --ink:#111;
  --orange:#f26a1b;
  --blue:#0a9ad9;
  --link-blue:#1a8fd6;
  --head-blue:#1d7fd1;
  --grey-band:#efefef;
  --text-grey:#6a6a6a;
  --title-grey:#555;
  --white:#fff;
  --footer:#121212;
  --bar:#050505;
}
*{box-sizing:border-box;margin:0;padding:0}
html,body{width:1200px;height:2200px;overflow:hidden}
body{background:var(--white);font-family:"Arimo",Arial,sans-serif;color:var(--ink);position:relative}
.container{width:1000px;margin:0 auto;position:relative}

/* header */
.site-header{position:absolute;top:0;left:0;width:1200px;height:80px;background:var(--black);z-index:2}
.site-header .container{display:flex;align-items:center;justify-content:space-between;height:80px}
.brand{display:flex;align-items:center;gap:14px;color:var(--white);font-family:"Source Sans 3",sans-serif;font-weight:600;font-size:44px;letter-spacing:3px}
.brand-mark{width:40px;height:40px;background:var(--white)}
.main-nav{display:flex;gap:38px}
.main-nav a{color:var(--white);text-decoration:none;font-size:16px}

/* hero */
.hero{position:absolute;top:0;left:0;width:1200px;height:613px;overflow:hidden}
.hero-photo{position:absolute;inset:0;background:linear-gradient(115deg,#2a2623 0%,#4a4039 30%,#1f2326 55%,#2c3a4c 75%,#121416 100%)}
.hero-content{position:absolute;top:196px;left:100px;width:480px}
.hero-title{font-family:"Source Sans 3",sans-serif;font-weight:400;color:var(--white);font-size:29px;line-height:36px}
.btn-primary{display:inline-block;margin-top:30px;background:var(--orange);color:var(--white);font-family:"Source Sans 3",sans-serif;font-size:22px;width:189px;height:48px;line-height:48px;text-align:center;border-radius:3px;text-decoration:none}
.scroll-cue{position:absolute;left:587px;top:553px}

/* intro */
.intro{position:absolute;top:613px;left:0;width:1200px;height:216px;background:var(--grey-band);display:flex;align-items:center;justify-content:center}
.intro p{width:980px;text-align:center;font-family:"Source Sans 3",sans-serif;font-size:27px;line-height:42px;color:#333}
.intro strong{color:var(--link-blue);font-weight:600}

/* features */
.features{position:absolute;top:829px;left:0;width:1200px;height:657px}
.feature-grid{position:absolute;left:70px;top:56px;width:1060px;display:grid;grid-template-columns:repeat(4,1fr);row-gap:66px}
.feature{text-align:center;width:230px;justify-self:center}
.feature-icon{width:123px;height:123px;border:3px solid var(--orange);border-radius:50%;margin:0 auto;display:flex;align-items:center;justify-content:center}
.feature-title{font-family:"Source Sans 3",sans-serif;font-weight:600;color:var(--title-grey);font-size:24px;margin-top:14px}
.feature-text{color:var(--text-grey);font-size:15px;line-height:22px;margin-top:8px}

/* testimonial */
.testimonial{position:absolute;top:1486px;left:0;width:1200px;height:333px;background:var(--blue);text-align:center;color:var(--white)}
.quote-badge{width:85px;height:85px;border-radius:50%;background:var(--orange);border:3px solid var(--white);margin:30px auto 0;display:flex;align-items:center;justify-content:center}
.quote-text{width:1000px;margin:28px auto 0;font-family:"Source Sans 3",sans-serif;font-weight:600;font-size:16px;line-height:24px}
.quote-author{margin-top:22px;font-family:"Source Sans 3",sans-serif;font-weight:700;font-size:15px;line-height:24px}

/* footer */
.site-footer{position:absolute;top:1819px;left:0;width:1200px;height:330px;background:var(--footer);color:var(--white)}
.footer-col{position:absolute;top:40px}
.footer-col h3{font-family:"Source Sans 3",sans-serif;font-weight:600;color:var(--head-blue);font-size:19px;margin-bottom:20px}
.col-contact{left:100px;width:240px}
.col-twitter{left:368px;width:220px}
.col-about{left:625px;width:220px}
.col-follow{left:867px;width:236px}
.contact-item{display:flex;gap:12px;align-items:flex-start;font-size:14px;line-height:19px;margin-bottom:28px}
.contact-item svg{flex:none;margin-top:1px}
.tweet{font-size:13px;line-height:15px;margin-bottom:16px;color:#ddd;padding-left:4px}
.tweet b{color:var(--white)}
.tweet .handle{color:#888;font-size:11px}
.tweet a{color:var(--link-blue);text-decoration:none}
.about-links{list-style:none}
.about-links li{font-size:13.5px;margin-bottom:14px}
.follow-text{font-size:13.5px;line-height:20px;text-align:justify}
.social-list{display:flex;gap:9px;margin-top:28px}
.social-list span{width:30px;height:30px;background:#555;display:block}
.social-list span.light{background:#bbb}

.bottom-bar{position:absolute;top:2149px;left:0;width:1200px;height:51px;background:var(--bar);color:var(--white);font-size:14px}
.bottom-bar .container{display:flex;justify-content:space-between;align-items:center;height:51px}
</style>
</head>
<body>

<section class="hero">
  <div class="hero-photo" role="img" aria-label="Dim photo of a person working on a laptop at a wooden desk"></div>
  <div class="hero-content">
    <h1 class="hero-title">We offer a social media monitoring service that works in a call centre environment</h1>
    <a class="btn-primary" href="#">Use it for free</a>
  </div>
  <svg class="scroll-cue" width="34" height="22" viewBox="0 0 34 22"><path d="M3 3 L17 17 L31 3" fill="none" stroke="#fff" stroke-width="4"/></svg>
</section>

<header class="site-header">
  <div class="container">
    <div class="brand"><span class="brand-mark"></span>TROVA</div>
    <nav class="main-nav">
      <a href="#">Home</a><a href="#">Trova Platform</a><a href="#">Trova Service</a><a href="#">Case Studies</a><a href="#">About Us</a><a href="#">Contact</a>
    </nav>
  </div>
</header>

<section class="intro">
  <p>simply dummy text of the printing and typesetting, industry. <strong>Lorem Ipsum has been the industry's standard dummy text</strong> ever since the 1500s, when an unknown printer took a galley of type...</p>
</section>

<section class="features">
  <div class="feature-grid">
    <div class="feature"><div class="feature-icon"><svg width="40" height="40" viewBox="0 0 40 40"><circle cx="20" cy="20" r="16" fill="#f26a1b"/><path d="M8 14 Q20 22 30 8 M12 32 Q18 20 34 24" stroke="#fff" stroke-width="2.5" fill="none"/></svg></div><h2 class="feature-title">Lorem ipsum</h2><p class="feature-text">Constantly crawling hundreds of Thousands of online sources</p></div>
    <div class="feature"><div class="feature-icon"><svg width="42" height="40" viewBox="0 0 42 40"><path d="M6 6 H36 Q39 6 39 9 V26 Q39 29 36 29 H20 L12 36 V29 H6 Q3 29 3 26 V9 Q3 6 6 6Z" fill="none" stroke="#f26a1b" stroke-width="3"/><circle cx="14" cy="18" r="2" fill="#f26a1b"/><circle cx="21" cy="18" r="2" fill="#f26a1b"/><circle cx="28" cy="18" r="2" fill="#f26a1b"/></svg></div><h2 class="feature-title">Lorem ipsum</h2><p class="feature-text">Constantly crawling hundreds of Thousands of online sources</p></div>
    <div class="feature"><div class="feature-icon"><svg width="44" height="44" viewBox="0 0 44 44"><g stroke="#f26a1b" stroke-width="2.5"><line x1="22" y1="22" x2="22" y2="6"/><line x1="22" y1="22" x2="6" y2="22"/><line x1="22" y1="22" x2="38" y2="22"/><line x1="22" y1="22" x2="10" y2="36"/><line x1="22" y1="22" x2="34" y2="36"/></g><g fill="#f26a1b"><circle cx="22" cy="22" r="6"/><circle cx="22" cy="6" r="3.5"/><circle cx="6" cy="22" r="3.5"/><circle cx="38" cy="22" r="3.5"/><circle cx="10" cy="36" r="3.5"/><circle cx="34" cy="36" r="3.5"/></g></svg></div><h2 class="feature-title">Lorem ipsum</h2><p class="feature-text">Constantly crawling hundreds of Thousands of online sources</p></div>
    <div class="feature"><div class="feature-icon"><svg width="48" height="32" viewBox="0 0 48 32"><circle cx="17" cy="16" r="11" fill="none" stroke="#f26a1b" stroke-width="4"/><circle cx="31" cy="16" r="11" fill="none" stroke="#f26a1b" stroke-width="4"/></svg></div><h2 class="feature-title">Lorem ipsum</h2><p class="feature-text">Constantly crawling hundreds of Thousands of online sources</p></div>
    <div class="feature"><div class="feature-icon"><svg width="36" height="44" viewBox="0 0 36 44"><g fill="none" stroke="#f26a1b" stroke-width="3"><circle cx="10" cy="6" r="3.5"/><circle cx="27" cy="22" r="3.5"/><circle cx="27" cy="36" r="3.5"/><path d="M10 10 V28 Q10 36 18 36 H23 M10 22 H23"/></g></svg></div><h2 class="feature-title">Lorem ipsum</h2><p class="feature-text">Constantly crawling hundreds of Thousands of online sources</p></div>
    <div class="feature"><div class="feature-icon"><svg width="38" height="42" viewBox="0 0 38 42"><path d="M6 2 H26 L34 10 V40 H6Z" fill="none" stroke="#f26a1b" stroke-width="2.5"/><rect x="1" y="20" width="36" height="13" fill="#f26a1b"/><text x="19" y="30.5" text-anchor="middle" font-family="Arimo,Arial,sans-serif" font-weight="700" font-size="10" fill="#fff">XML</text></svg></div><h2 class="feature-title">Lorem ipsum</h2><p class="feature-text">Constantly crawling hundreds of Thousands of online sources</p></div>
    <div class="feature"><div class="feature-icon"><svg width="46" height="40" viewBox="0 0 46 40"><g fill="none" stroke="#f26a1b" stroke-width="2.5" stroke-linejoin="round"><path d="M8 14 L23 8 L38 14 L23 20Z"/><path d="M8 14 V30 L23 37 L38 30 V14"/><path d="M23 20 V37"/><path d="M8 14 L2 21 L17 27 L23 20 M38 14 L44 21 L29 27 L23 20"/></g></svg></div><h2 class="feature-title">Lorem ipsum</h2><p class="feature-text">Constantly crawling hundreds of Thousands of online sources</p></div>
    <div class="feature"><div class="feature-icon"><svg width="30" height="44" viewBox="0 0 30 44"><text x="15" y="36" text-anchor="middle" font-family="Arimo,Arial,sans-serif" font-weight="700" font-size="38" fill="#f26a1b">$</text></svg></div><h2 class="feature-title">Lorem ipsum</h2><p class="feature-text">Constantly crawling hundreds of Thousands of online sources</p></div>
  </div>
</section>

<section class="testimonial">
  <div class="quote-badge"><svg width="38" height="30" viewBox="0 0 38 30"><path d="M2 2 H16 V16 Q16 26 6 28 L5 24 Q10 22 10 16 H2Z M22 2 H36 V16 Q36 26 26 28 L25 24 Q30 22 30 16 H22Z" fill="#fff"/></svg></div>
  <p class="quote-text">"Kestrel help us to find new potential customers and also to deepen existing customer relationships. Scent desire to customize exactly to our needs service tool has been ihaltavaa "Kestrel help us to find new potential customers and also to deepen existing customer relationships. Scent desire to customize exactly to our needs service tool has been ihaltavaa""</p>
  <p class="quote-author">Written By<br>AINO RASKELA, SALES MANAGER, NORTHMERE LTD</p>
</section>

<footer class="site-footer">
  <div class="footer-col col-contact">
    <h3>Contact us</h3>
    <div class="contact-item"><svg width="18" height="18" viewBox="0 0 18 18"><circle cx="9" cy="9" r="8" fill="none" stroke="#1d7fd1" stroke-width="1.6"/><path d="M6 5 L8 5 L8.5 7.5 L7.5 8.5 Q8.5 10 9.5 10.5 L10.5 9.5 L13 10 L13 12 Q9 13 6 9 Q5 7 6 5Z" fill="#1d7fd1"/></svg>01 4820 3391 (Phone)</div>
    <div class="contact-item"><svg width="20" height="16" viewBox="0 0 20 16"><path d="M1 6 Q10 0 19 6 L17 9 L14 7 L14 5 Q10 3 6 5 L6 7 L3 9Z" fill="#1d7fd1"/><rect x="4" y="9" width="12" height="6" rx="1" fill="#1d7fd1"/></svg>01 4820 3391 (Fax)</div>
    <div class="contact-item"><svg width="18" height="14" viewBox="0 0 18 14"><rect x="1" y="1" width="16" height="12" fill="#1d7fd1"/><path d="M1 1 L9 8 L17 1" fill="none" stroke="#121212" stroke-width="1.4"/></svg>hello@trovamail.ie</div>
    <div class="contact-item"><svg width="16" height="20" viewBox="0 0 16 20"><path d="M8 1 Q14 1 14 7 Q14 11 8 19 Q2 11 2 7 Q2 1 8 1Z" fill="#1d7fd1"/><circle cx="8" cy="7" r="2.5" fill="#121212"/></svg>PO Box : 4417, Galway Lorem ipsum dollor si3844</div>
  </div>
  <div class="footer-col col-twitter">
    <h3>Twitter Feed</h3>
    <p class="tweet"><b>Orla</b> <span class="handle">@orlawrites</span><br>How to Download Photos from Post task to take photos from Postbin to... <a href="#">pstb.in/k4Rq8Lm2</a></p>
    <p class="tweet"><b>Orla</b> <span class="handle">@orlawrites</span><br>How to Download Photos from Post task to take photos from Postbin to... <a href="#">pstb.in/k4Rq8Lm2</a></p>
    <p class="tweet"><b>Orla</b> <span class="handle">@orlawrites</span><br>How to Download Photos from Post task to take photos from Postbin to... <a href="#">pstb.in/k4Rq8Lm2</a></p>
  </div>
  <div class="footer-col col-about">
    <h3>About Us</h3>
    <ul class="about-links">
      <li>Investor</li><li>Careers</li><li>Terms &amp; Conditions of Services</li><li>Privacy Policy</li><li>Services Level Agreement</li><li>Master Commerical Agfrement</li>
    </ul>
  </div>
  <div class="footer-col col-follow">
    <h3>Follow Us</h3>
    <p class="follow-text">Lorem Ipsum is simply dummy text of the printing and typesetting industry. Lorem Ipsum has been the industry's standard dummy text ever since the 1500s,</p>
    <div class="social-list"><span></span><span></span><span></span><span></span><span class="light"></span><span></span></div>
  </div>
</footer>

<div class="bottom-bar">
  <div class="container">
    <span>© Copyright 2015, trova, Inc. All rights reserved.</span>
    <span>Site Map | Legal | Privacy | Cookies</span>
  </div>
</div>

</body>
</html>
```